Design mobile friendly real estate and property management company landing page

Design a clean, crisp modern looking landing page that is mobile-friendly (must resize, preferably using bootstrap framework). Landing page will consist of heading with login area, company info, body consists of company description and services, a list of available rental properties with photos, and a footer with additional links and info. Working on updating with text for text areas marked A, B, and C on the layout pdf, but in meantime, lorem ipsum is fine. I can connect events to most buttons, etc. Just need the bootstrap and html functionality set up. Previous company website (which should not be relied upon) is www.qlbt.net This is somewhat of a template for a start, but looking for a more professional and modern design for the new website. But this gives an idea of the content and what needs to be displayed, and how.

Target Market(s)

Clients looking for a property management company that is efficient and well-organized.

Industry/Entity Type

Property Management

Coding

Coded - Design and coding required

Number of Pages Required

1 page

Font styles to use
Sans Serif

Colors
0355a3

Requirements
Must have
• Resize for the screen using bootstrap.
• Navigation that collapses for mobile devices
• Large text boxes and good solid spacing around all elements.
Nice to have
• for property images it would be nice if they can be swiped on touch enabled devices (to the next or previous image). And have navigation that can be clicked to next or previous images.
• Would be nice if a captcha verification was included on contact form.
Should not have
• Fancy or eccentric art

```html
<!DOCTYPE html>
<html lang="en">
<head>
<meta charset="utf-8">
<title>Harborline Realty Services</title>
<link href="https://fonts.googleapis.com/css2?family=Open+Sans:ital,wght@0,400;0,600;0,700;1,400&display=swap" rel="stylesheet">
<style>
:root{
  --brand:#0355a3;
  --navy:#141c33;
  --ink:#1e2433;
  --muted:#777c86;
  --line:#e4e6ea;
  --band:#f1f3f6;
  --white:#ffffff;
}
*{box-sizing:border-box;margin:0;padding:0}
html,body{width:1200px;height:2190px;overflow:hidden}
body{position:relative;background:var(--white);font-family:'Open Sans',sans-serif;color:var(--ink)}
.abs{position:absolute}

.topbar{left:0;top:0;width:1200px;height:93px;border-top:2px solid var(--navy);background:var(--white)}
.brand-name{left:86px;top:24px;font-size:22px;font-weight:600;letter-spacing:2px;color:var(--navy);line-height:1.25}
.filter{left:652px;top:26px;width:319px;height:44px;background:#f3f4f6;border:1px solid #dfe1e5;border-radius:3px;font-size:12px;color:#888;padding:13px 14px}
.filter svg{position:absolute;right:14px;top:19px}
.login{left:980px;top:26px;width:134px;height:44px;background:var(--navy);color:var(--white);border-radius:3px;font-size:15px;font-weight:600;display:flex;align-items:center;justify-content:center;gap:8px}

.mainnav{left:0;top:93px;width:1200px;height:53px;background:var(--brand)}
.mainnav ul{list-style:none;display:flex;position:absolute;left:86px;top:0;height:53px}
.mainnav li{color:var(--white);font-size:12px;height:53px;display:flex;align-items:center;padding:0 34px}
.mainnav li.active{background:var(--navy)}
.mainnav li:nth-child(n+2){padding:0 34px 0 40px}

.hero{left:0;top:146px;width:1200px;height:504px;background:linear-gradient(180deg,#7fb0df 0%,#c9dcef 30%,#b6a89a 55%,#6e9a48 78%,#4e8a34 100%)}
.welcome{left:86px;top:314px;width:425px;height:172px;background:rgba(40,44,56,.82);padding:26px 24px}
.welcome h1{color:var(--white);font-size:22px;font-weight:700;letter-spacing:.5px;margin-bottom:14px}
.welcome p{color:var(--white);font-size:11.5px;font-style:italic;line-height:24px}
.dots{left:100px;top:624px;display:flex;gap:5px}
.dots i{width:10px;height:10px;border-radius:50%;background:var(--navy)}
.dots i.on{background:#3a8ad6}

.contact{left:825px;top:323px;width:289px;height:394px;background:var(--brand);border:2px solid #e8eef6;padding:14px 13px}
.contact h2{color:var(--white);text-align:center;font-size:20px;font-weight:600;margin-bottom:14px}
.field{background:var(--white);height:34px;border-radius:3px;font-size:11px;color:#777;padding:10px 12px;margin-bottom:8px}
.field.tall{height:82px}
.send{display:block;margin:16px auto 0;width:124px;height:37px;background:var(--navy);color:var(--white);font-size:15px;font-weight:600;text-align:center;line-height:37px;border-radius:3px}

.badges{left:0;top:650px;width:1200px;height:121px;background:var(--band)}
.badge{top:667px;width:171px;height:92px;background:var(--white);border:2px solid #dfe2e6;border-radius:5px;display:flex;align-items:center;justify-content:center}
.badge span{width:110px;height:52px;border-radius:4px;background:#d7dde5}

.service{top:809px;width:489px;height:371px;background:var(--white);border:2px solid #eceef1;padding:10px}
.service .photo{width:100%;height:212px}
.service h3{color:var(--brand);font-size:15px;font-weight:600;margin:20px 2px 14px}
.service p{font-size:11.5px;color:var(--muted);line-height:24px;margin:0 2px}

.listings{left:0;top:1219px;width:1200px;height:755px;background:var(--band)}
.sec-title{left:0;top:1252px;width:1200px;text-align:center;font-size:23px;font-weight:700;color:var(--navy)}
.sec-lead{left:250px;top:1290px;width:700px;text-align:center;font-size:11.5px;color:var(--muted);line-height:23px}

.listing{left:86px;width:1028px;height:235px;background:var(--white);border:1px solid #e0e3e7}
.listing .photo{position:absolute;left:0;top:0;width:305px;height:235px}
.tag{position:absolute;left:0;top:0;width:127px;height:38px;background:var(--brand);color:var(--white);font-size:16px;font-weight:700;padding:8px 0 0 26px}
.arrow{position:absolute;top:106px;width:26px;height:26px;border:1.5px solid var(--white);border-radius:50%;display:flex;align-items:center;justify-content:center}
.bar{position:absolute;top:0;height:45px;background:var(--navy);color:var(--white);font-size:11.5px;display:flex;align-items:center;gap:10px;padding-left:20px}
.bar .ico{width:26px;height:26px;border:1.5px solid var(--white);border-radius:50%;display:flex;align-items:center;justify-content:center}
.specs{position:absolute;left:305px;top:45px;width:362px;height:190px}
.specs .row{display:flex;height:47.5px;border-bottom:1px solid #eceef1;font-size:12px;color:#555;align-items:center}
.specs .row:last-child{border-bottom:0}
.specs .row span{width:181px;padding-left:40px}
.desc{position:absolute;left:667px;top:45px;width:361px;height:190px;border-left:1px solid #eceef1;padding:14px 14px;font-size:11.5px;font-style:italic;color:var(--muted);line-height:24.5px}

.footer{left:0;top:1974px;width:1200px;height:216px;background:var(--brand)}
.socials{left:390px;top:2006px;display:flex;gap:14px}
.socials i{width:59px;height:59px;border-radius:50%;background:rgba(255,255,255,.08);border:1px solid rgba(255,255,255,.15);display:flex;align-items:center;justify-content:center}
.socials i b{width:14px;height:14px;border-radius:50%;background:var(--white)}
.footnav{left:0;top:2090px;width:1200px;display:flex;justify-content:center;color:var(--white);font-size:12px}
.footnav span{padding:0 24px;border-left:1px solid var(--white);line-height:12px}
.footnav span:first-child{border-left:0}
.copy{left:0;top:2137px;width:1200px;text-align:center;color:var(--white);font-size:10px}
</style>
</head>
<body>

<header class="abs topbar">
  <div class="abs brand-name">HARBORLINE REALTY<br><span style="font-size:14px;letter-spacing:6px;padding-left:52px">SERVICES</span></div>
  <div class="abs filter">Wight Filter :
    <svg width="10" height="6" viewBox="0 0 10 6"><path d="M0 0h10L5 6z" fill="#888"/></svg>
  </div>
  <div class="abs login">
    <svg width="14" height="14" viewBox="0 0 14 14"><path d="M1 6h7V3l4 4-4 4V8H1z" fill="#fff"/><path d="M8 1h5v12H8" stroke="#fff" stroke-width="1.6" fill="none"/></svg>
    LOGIN
  </div>
</header>

<nav class="abs mainnav">
  <ul>
    <li class="active">HOME</li><li>FOR RENT</li><li>FOR SALE</li><li>PROPERTY MANAGEMENT</li><li>REAL ESTATE</li><li>ABOUT US</li><li>CONTACT US</li>
  </ul>
</nav>

<section class="abs hero" role="img" aria-label="Large suburban house with lawn and garden under a blue sky"></section>
<div class="abs welcome">
  <h1>WELCOME TO&nbsp; OUR COMPANY</h1>
  <p>We are a locally owned and operated San Diego Property Management company. Serving all areas of San Diego County, we provide personal, management services for all types of residential property.</p>
</div>
<div class="abs dots"><i></i><i></i><i class="on"></i><i></i><i></i></div>

<section class="abs badges"></section>
<div class="abs badge" style="left:89px"><span></span></div>
<div class="abs badge" style="left:293px"><span></span></div>
<div class="abs badge" style="left:498px"><span></span></div>

<form class="abs contact">
  <h2>CONTACT US</h2>
  <div class="field">Name :</div>
  <div class="field">Phone :</div>
  <div class="field">Email :</div>
  <div class="field">Subject Property :</div>
  <div class="field tall">Comments :</div>
  <span class="send">SEND NOW</span>
</form>

<article class="abs service" style="left:86px">
  <div class="photo" role="img" aria-label="Two-storey family home with flower garden and for-sale sign" style="background:linear-gradient(180deg,#b9c6d2,#a69a86 55%,#6f8f4e)"></div>
  <h3>PROPERTY MANAGEMENT</h3>
  <p>We are a locally owned and operated San Diego Property Management company. Serving all areas of San Diego County, we provide personal, reliable property man-agement services for all types of residential property.</p>
</article>
<article class="abs service" style="left:626px">
  <div class="photo" role="img" aria-label="Large brick manor house surrounded by trees" style="background:linear-gradient(180deg,#9cc3e8,#b39670 50%,#5f8a3c)"></div>
  <h3>REAL ESTATE</h3>
  <p>We are a locally owned and operated San Diego Property Management company. Serving all areas of San Diego County, we provide personal, reliable property man-agement services for all types of residential property.</p>
</article>

<section class="abs listings"></section>
<h2 class="abs sec-title">FEATURED LISTINGS</h2>
<p class="abs sec-lead">We are a locally owned and operated San Diego Property Management company. Serving all areas of San Diego County, we reliable property management services for all types of residential property.</p>

<article class="abs listing" style="top:1369px">
  <div class="photo" role="img" aria-label="Townhouses with garages and a parked pickup truck" style="background:linear-gradient(180deg,#6fa5d8,#a08a6c 45%,#8c8c88)"></div>
  <div class="tag">FOR RENT</div>
  <div class="arrow" style="left:10px"><svg width="8" height="10" viewBox="0 0 8 10"><path d="M6 1L2 5l4 4" stroke="#fff" stroke-width="1.6" fill="none"/></svg></div>
  <div class="arrow" style="left:269px"><svg width="8" height="10" viewBox="0 0 8 10"><path d="M2 1l4 4-4 4" stroke="#fff" stroke-width="1.6" fill="none"/></svg></div>
  <div class="bar" style="left:305px;width:362px"><span class="ico"><svg width="10" height="13" viewBox="0 0 10 13"><path d="M5 0a5 5 0 0 1 5 5c0 3-5 8-5 8S0 8 0 5a5 5 0 0 1 5-5z" fill="#fff"/><circle cx="5" cy="5" r="1.8" fill="#141c33"/></svg></span>1187 Larkmoor Ave San Diego, CA 92104</div>
  <div class="bar" style="left:667px;width:361px"><span class="ico"><svg width="14" height="10" viewBox="0 0 14 10"><path d="M1 0v10M1 7h12v3M1 4h5a2 2 0 0 1 2 2v1M8 4h4a1 1 0 0 1 1 1v2" stroke="#fff" stroke-width="1.5" fill="none"/></svg></span>2 Bedroom, 1 Bath Condo</div>
  <div class="specs">
    <div class="row"><span>RENT</span><span>COMMUNITY</span></div>
    <div class="row"><span>AVAILABLE</span><span>PARKING</span></div>
    <div class="row"><span>SQFT</span><span>PETS</span></div>
    <div class="row"><span>LEASE</span><span>LAUNDRY</span></div>
  </div>
  <p class="desc">We are a locally owned and operated San Diego Property Man-agement company. Serving all areas of San Diego County, we reliable property management services for all types of residen-tial property.Highly upgraded 2BR/1BA condo in gated North Park community. Unit features hardwood flooring, granite Must have excellent rental history....</p>
</article>

<article class="abs listing" style="top:1656px">
  <div class="photo" role="img" aria-label="Tan stucco two-storey house with garage" style="background:linear-gradient(180deg,#3f86d6,#c7a06a 50%,#a88452)"></div>
  <div class="tag">FOR SALE</div>
  <div class="arrow" style="left:10px"><svg width="8" height="10" viewBox="0 0 8 10"><path d="M6 1L2 5l4 4" stroke="#fff" stroke-width="1.6" fill="none"/></svg></div>
  <div class="arrow" style="left:269px"><svg width="8" height="10" viewBox="0 0 8 10"><path d="M2 1l4 4-4 4" stroke="#fff" stroke-width="1.6" fill="none"/></svg></div>
  <div class="bar" style="left:305px;width:362px"><span class="ico"><svg width="10" height="13" viewBox="0 0 10 13"><path d="M5 0a5 5 0 0 1 5 5c0 3-5 8-5 8S0 8 0 5a5 5 0 0 1 5-5z" fill="#fff"/><circle cx="5" cy="5" r="1.8" fill="#141c33"/></svg></span>1187 Larkmoor Ave San Diego, CA 92104</div>
  <div class="bar" style="left:667px;width:361px"><span class="ico"><svg width="14" height="10" viewBox="0 0 14 10"><path d="M1 0v10M1 7h12v3M1 4h5a2 2 0 0 1 2 2v1M8 4h4a1 1 0 0 1 1 1v2" stroke="#fff" stroke-width="1.5" fill="none"/></svg></span>2 Bedroom, 1 Bath Condo</div>
  <div class="specs">
    <div class="row"><span>RENT</span><span>COMMUNITY</span></div>
    <div class="row"><span>AVAILABLE</span><span>PARKING</span></div>
    <div class="row"><span>SQFT</span><span>PETS</span></div>
    <div class="row"><span>LEASE</span><span>LAUNDRY</span></div>
  </div>
  <p class="desc">We are a locally owned and operated San Diego Property Man-agement company. Serving all areas of San Diego County, we reliable property management services for all types of residen-tial property.Highly upgraded 2BR/1BA condo in gated North Park community. Unit features hardwood flooring, granite Must have excellent rental history....</p>
</article>

<footer class="abs footer"></footer>
<div class="abs socials">
  <i><b></b></i><i><b></b></i><i><b></b></i><i><b></b></i><i><b></b></i>
  <i><svg width="18" height="13" viewBox="0 0 18 13"><rect x="1" y="1" width="16" height="11" rx="1.5" stroke="#fff" stroke-width="1.6" fill="none"/><path d="M1 2l8 6 8-6" stroke="#fff" stroke-width="1.6" fill="none"/></svg></i>
</div>
<div class="abs footnav"><span>HOME</span><span>FOR RENT</span><span>FOR SALE</span><span>PROPERTY MANAGEMENT</span><span>REAL ESTATE</span><span>ABOUT US</span><span>CONTACT US</span></div>
<p class="abs copy">© COPY RIGHT 2016 HARBORLINE REALTY &amp; MANAGEMENT ALL RIGHTS RESERVED</p>

</body>
</html>
```